Business Card Design

I want something very modern, Im from the gold coast Australia double sided and using my attached logo, a mix of cameras or a close up, I will attach pics, no logo please from other manufacturers, only Guard Every Door, I want to promote a individual approach to security, My logo is - Honest Advise Without The Price - :)

Target Market(s)

Anyone that handles money or wants to secure there premises

Industry/Entity Type

Business

Contact Information for Business Card

Marcus Dell pikeford
Guard Every Door
Elmvale Queensland 4219
Mobile : 0431 586 902 & Skype +610431586902
Security Provider Licence QLD - 5842913
Free Quotes
CCTV, Alarms, Digital Cameras, RFID, - In Home Design

Colors

Designer to choose colors to be used in the design.

Requirements
Must have
• Free Quotes
On Site Design
Full details And Licence number Etc
Should not have
• I know these are low res pics, im waiting to receive stock before taking new photos

```html
<!DOCTYPE html>
<html lang="en">
<head>
<meta charset="utf-8">
<title>Guard Every Door – Business Card</title>
<link rel="stylesheet" href="https://fonts.googleapis.com/css2?family=Open+Sans:wght@400;600;700&display=swap">
<style>
  :root {
    --stage: #b3b3b3;
    --card-black: #0b0b0b;
    --white: #ffffff;
    --red: #e3191f;
    --red-dark: #a10f14;
    --grey-mid: #8a8a8a;
    --text-dark: #1a1a1a;
    --logo-grey: #3a3a3a;
    --photo-sea: #2f7fa8;
    --photo-city: #3c3a3f;
  }
  * { margin: 0; padding: 0; box-sizing: border-box; }
  html, body { width: 1200px; height: 900px; overflow: hidden; }
  body {
    background: var(--stage);
    font-family: "Open Sans", Arial, sans-serif;
    position: relative;
  }
  .card {
    position: absolute;
    top: 290px;
    width: 533px;
    height: 319px;
    background: var(--card-black);
    overflow: hidden;
    color: var(--white);
  }
  .card--front { left: 48px; }
  .card--back { left: 614px; }
  .card__art { position: absolute; inset: 0; width: 533px; height: 319px; }

  .card__headline {
    position: absolute; left: 0; right: 0; text-align: center;
  }
  .licence { top: 15px; font-size: 14px; font-weight: 400; }
  .tagline { top: 286px; font-size: 14px; font-weight: 700; letter-spacing: 0.1px; }
  .supply-title { top: 14px; font-size: 18px; font-weight: 400; }

  .brand-name {
    position: absolute;
    font-weight: 700;
    text-transform: uppercase;
    line-height: 1.05;
    display: flex; align-items: center; gap: 7px;
  }
  .brand-name__mark { width: 10px; height: 10px; background: var(--red); flex: none; }
  .card--front .brand-name { left: 74px; top: 172px; font-size: 19px; color: var(--logo-grey); }
  .card--back .brand-name { left: 18px; top: 270px; font-size: 11px; color: var(--white); gap: 5px; }
  .card--back .brand-name__mark { width: 7px; height: 7px; }

  .contact { position: absolute; left: 269px; top: 95px; color: var(--text-dark); }
  .contact__name { font-size: 18px; font-weight: 700; letter-spacing: 0.2px; }
  .contact__role { font-size: 13px; margin-top: 0; }
  .contact__list { list-style: none; margin-top: 8px; }
  .contact__item {
    display: flex; align-items: center; gap: 7px;
    font-size: 13px; height: 19px; letter-spacing: 0.3px;
  }
  .contact__icon { width: 15px; height: 15px; flex: none; }

  .photo-band {
    position: absolute; left: 0; top: 0; width: 533px; height: 319px;
  }
  .services {
    position: absolute; list-style: none; font-size: 13px; line-height: 19px;
  }
  .services li::before { content: "•"; margin-right: 6px; }
  .services--a { left: 116px; top: 251px; }
  .services--b { left: 219px; top: 251px; }
  .services--c { left: 344px; top: 290px; }
</style>
</head>
<body>

<section class="card card--front" aria-label="Business card front">
  <svg class="card__art" viewBox="0 0 533 319" aria-hidden="true">
    <defs>
      <linearGradient id="redSweep" x1="0" x2="1">
        <stop offset="0" stop-color="#ffffff"/>
        <stop offset="0.45" stop-color="#e3191f"/>
        <stop offset="1" stop-color="#c4141a"/>
      </linearGradient>
      <linearGradient id="greySweep" x1="0" x2="1">
        <stop offset="0" stop-color="#111"/>
        <stop offset="0.6" stop-color="#8a8a8a"/>
        <stop offset="1" stop-color="#eeeeee"/>
      </linearGradient>
    </defs>
    <path d="M0,62 Q250,20 533,82 L533,232 Q270,290 0,226 Z" fill="#ffffff"/>
    <path d="M200,44 Q430,40 533,78 L533,104 Q420,62 240,50 Z" fill="url(#redSweep)"/>
    <path d="M0,232 Q240,290 470,262 Q300,276 0,240 Z" fill="url(#greySweep)"/>
  </svg>

  <p class="card__headline licence">Security Provider Licence QLD - 5842913</p>

  <div class="brand-name"><span class="brand-name__mark"></span><span>Guard<br>Every Door</span></div>

  <div class="contact">
    <h1 class="contact__name">MARCUS DELL PIKEFORD</h1>
    <p class="contact__role">Security Advisor</p>
    <ul class="contact__list">
      <li class="contact__item">
        <svg class="contact__icon" viewBox="0 0 15 15" aria-hidden="true"><circle cx="7.5" cy="7.5" r="7.5" fill="var(--red)"/><rect x="5" y="3" width="5" height="9" rx="1" fill="#fff"/><rect x="5.8" y="4" width="3.4" height="6" fill="var(--red)"/></svg>
        0431 586 902
      </li>
      <li class="contact__item">
        <svg class="contact__icon" viewBox="0 0 15 15" aria-hidden="true"><circle cx="7.5" cy="7.5" r="7.5" fill="var(--red)"/></svg>
        +610431586902
      </li>
      <li class="contact__item">
        <svg class="contact__icon" viewBox="0 0 15 15" aria-hidden="true"><circle cx="7.5" cy="7.5" r="7.5" fill="var(--red)"/><rect x="3.5" y="4.5" width="8" height="6" fill="#fff"/><path d="M3.5,4.5 L7.5,8 L11.5,4.5" fill="none" stroke="var(--red)" stroke-width="1"/></svg>
        guardeverydoor@mailhub.com
      </li>
      <li class="contact__item">
        <svg class="contact__icon" viewBox="0 0 15 15" aria-hidden="true"><circle cx="7.5" cy="7.5" r="7.5" fill="var(--red)"/><path d="M7.5,12 L4.6,7.6 A3.3,3.3 0 1 1 10.4,7.6 Z" fill="#fff"/><circle cx="7.5" cy="6" r="1.2" fill="var(--red)"/></svg>
        Elmvale Queensland 4219
      </li>
    </ul>
  </div>

  <p class="card__headline tagline">HONEST ADVICE WITHOUT THE PRICE</p>
</section>

<section class="card card--back" aria-label="Business card back">
  <svg class="card__art" viewBox="0 0 533 319" aria-hidden="true">
    <defs>
      <linearGradient id="backRed" x1="0" x2="1">
        <stop offset="0" stop-color="#e3191f" stop-opacity="0.2"/>
        <stop offset="0.4" stop-color="#e3191f"/>
        <stop offset="1" stop-color="#c4141a"/>
      </linearGradient>
      <linearGradient id="backGrey" x1="0" x2="1">
        <stop offset="0" stop-color="#5a5a5a"/>
        <stop offset="1" stop-color="#1a1a1a"/>
      </linearGradient>
    </defs>
    <path d="M180,52 Q420,50 533,96 L533,122 Q420,72 210,58 Z" fill="url(#backRed)"/>
    <path d="M0,130 Q150,220 400,232 Q200,236 0,150 Z" fill="url(#backGrey)"/>
  </svg>

  <p class="card__headline supply-title">Buy Direct From The QLD Supplier</p>

  <svg class="photo-band" viewBox="0 0 533 319" role="img" aria-label="Photo of Gold Coast beachfront city skyline with security cameras and an intercom unit">
    <defs>
      <linearGradient id="photoTone" x1="0" x2="1" y1="0" y2="1">
        <stop offset="0" stop-color="var(--photo-sea)"/>
        <stop offset="0.45" stop-color="#6f8ea0"/>
        <stop offset="0.7" stop-color="var(--photo-city)"/>
        <stop offset="1" stop-color="#222"/>
      </linearGradient>
    </defs>
    <path d="M0,72 Q200,50 420,78 Q500,92 533,110 L533,226 Q420,235 330,232 Q120,220 0,130 Z" fill="url(#photoTone)"/>
  </svg>

  <div class="brand-name"><span class="brand-name__mark"></span><span>Guard<br>Every Door</span></div>

  <ul class="services services--a">
    <li>Free Quotes</li>
    <li>CCTV</li>
    <li>Alarms</li>
  </ul>
  <ul class="services services--b">
    <li>Digital Cameras</li>
    <li>RFID</li>
    <li>Onsite Design</li>
  </ul>
  <ul class="services services--c">
    <li>Local Supply and Warranty</li>
  </ul>
</section>

</body>
</html>
```